Website Revamp for 7K Distributor

Brovin Pte Ltd (http://brovin.com.sg/about.php) is a 7K authorized distributor located in Singapore.

The revamp hopes to move the look & feel of the website from a corporate/industrial feel to one that is more homely/interior-design, so as to attract architects, home-builders, interior-designers with a more up-market design.
Updates

If product images are required, please use images from www.brovin.com.sg. Thanks!

For newsletter signup, just a link at the header will do, as we will be implementing additional profiling fields in the signup form.

Target Market(s)

Hopes to attract architects, home-builders, interior-designers with a more up-market design.

Industry/Entity Type

Industrial

Requirements
Must have
• Refer to brief document

```html
<!DOCTYPE html>
<html lang="en">
<head>
<meta charset="utf-8">
<title>Brovin – Home</title>
<link href="https://fonts.googleapis.com/css2?family=Arimo:wght@400;700&family=PT+Sans:wght@400;700&family=Gelasio:wght@400;700&display=swap" rel="stylesheet">
<style>
:root{
  --brown-dark:#3f1c0a;
  --brown-mid:#6e3414;
  --brown-glow:#8a4519;
  --grey-bg:#e3e3e3;
  --white:#ffffff;
  --blue:#1a8fd6;
  --blue-text:#1b6eb5;
  --red:#c4200f;
  --orange:#e8501a;
  --gold:#f2a531;
  --badge-orange:#d97a12;
  --text:#4a4a4a;
  --text-light:#f0e6dc;
}
*{margin:0;padding:0;box-sizing:border-box}
html,body{width:1200px;height:1184px;overflow:hidden}
body{position:relative;background:var(--grey-bg);font-family:"Arimo",Arial,sans-serif;color:var(--text)}
.band-top{position:absolute;left:0;top:0;width:1200px;height:504px;
  background:radial-gradient(ellipse 520px 320px at 600px 0,var(--brown-glow),var(--brown-mid) 45%,var(--brown-dark) 100%)}
.band-footer{position:absolute;left:0;top:996px;width:1200px;height:188px;
  background:radial-gradient(ellipse 560px 200px at 600px 0,var(--brown-mid),var(--brown-dark) 100%);
  box-shadow:0 -4px 10px rgba(0,0,0,.25)}

/* header */
.header{position:absolute;left:142px;top:29px;width:918px;height:124px;background:var(--white);border-radius:6px;box-shadow:0 2px 6px rgba(0,0,0,.35)}
.logo-tab{position:absolute;left:142px;top:8px;width:268px;height:60px;background:var(--white);border-radius:8px 40px 0 0}
.logo{position:absolute;left:162px;top:26px;font-family:"Arimo",Arial,sans-serif;font-weight:700;font-size:44px;letter-spacing:-1px;color:var(--blue-text);line-height:1}
.top-links{position:absolute;top:42px;left:643px;display:flex}
.top-link{height:34px;display:flex;align-items:center;justify-content:center;gap:8px;padding:0 6px;background:linear-gradient(#fafafa,#e6e6e6);border:1px solid #d4d4d4;border-radius:4px;font-size:13px;color:#444;white-space:nowrap}
.top-link svg{flex:none}

/* nav */
.nav{position:absolute;left:142px;top:88px;width:918px;height:64px;display:flex}
.nav-home{width:60px;height:64px;background:linear-gradient(#e04a22,#b71e0a);display:flex;align-items:center;justify-content:center;border-radius:0 0 0 6px}
.nav-item{height:64px;padding:14px 0 0 12px;background:linear-gradient(#2aa6ea,#0c77c6);color:var(--white);border-left:1px solid #5cc0f2;font-family:"PT Sans",Arial,sans-serif;white-space:nowrap}
.nav-item b{display:block;font-size:17px;font-weight:700;line-height:18px;text-transform:uppercase}
.nav-item span{display:block;font-size:12px;line-height:14px;text-transform:uppercase}
.nav-item.active{background:linear-gradient(#d2311a,#b41d0a);border-left-color:#d8503a;height:72px}
.nav-item.last{border-radius:0 0 6px 0}

.dropdown{position:absolute;left:354px;top:160px;width:222px;background:var(--red);box-shadow:0 3px 8px rgba(0,0,0,.35);padding-bottom:4px}
.dropdown li,.submenu li{list-style:none;height:30px;line-height:30px;padding-left:20px;color:var(--white);font-size:13px;position:relative;white-space:nowrap}
.dropdown li::after{content:"";position:absolute;right:16px;top:12px;border-left:5px solid #fff;border-top:4px solid transparent;border-bottom:4px solid transparent}
.dropdown li.current{background:var(--blue)}
.submenu{position:absolute;left:580px;top:160px;width:159px;background:rgba(200,30,14,.95);padding-bottom:2px}
.submenu li{padding-left:23px}

/* slider */
.slider{position:absolute;left:140px;top:168px;width:921px;height:372px;background:var(--white);border-radius:6px;box-shadow:0 1px 5px rgba(0,0,0,.35)}
.slide-photo{position:absolute;left:151px;top:178px;width:899px;height:351px;
  background:linear-gradient(180deg,#c8d3d4 0%,#a9b2b0 40%,#5b5e5c 62%,#cfd2d0 78%,#e9eaea 100%)}
.slide-title{position:absolute;left:151px;top:208px;width:210px;height:48px;background:rgba(255,255,255,.85);font-family:"PT Sans",Arial,sans-serif;font-weight:700;font-size:26px;color:var(--blue-text);padding:8px 0 0 14px;white-space:nowrap;overflow:hidden}
.slide-dots{position:absolute;left:1006px;top:448px;display:flex;gap:2px}
.slide-dots i{width:10px;height:10px;background:#ddd;display:block}
.slide-dots i:last-child{background:#fff}
.slide-caption{position:absolute;left:151px;top:467px;width:899px;height:62px;background:rgba(40,40,40,.82);color:#eee;font-size:12.5px;line-height:19px;padding:11px 12px}

/* content */
.content{position:absolute;left:140px;top:558px;width:921px;height:410px;background:var(--white);border-radius:6px;box-shadow:0 1px 5px rgba(0,0,0,.3)}
.portfolio-photo{position:absolute;left:160px;top:577px;width:422px;height:372px;
  background:linear-gradient(180deg,#2f5fb0 0%,#6b93d2 35%,#a8b59c 55%,#4f8a3a 75%,#9a9a94 100%)}
.portfolio-badge{position:absolute;left:414px;top:598px;width:152px;height:84px;background:var(--badge-orange);border:3px solid #fff;border-radius:42px;box-shadow:0 2px 5px rgba(0,0,0,.35);color:var(--white);font-family:"PT Sans",Arial,sans-serif;font-weight:700;font-size:20px;line-height:20px;text-align:center;padding-top:19px;letter-spacing:.5px}
.view-more{position:absolute;left:499px;top:924px;width:83px;height:25px;background:#fff;border:1px solid #bbb;font-size:12px;color:#555;display:flex;align-items:center;justify-content:center;gap:5px;white-space:nowrap}

.hot{position:absolute;left:619px;top:577px;width:423px;height:372px;background:#ededed;border:1px solid #ddd;border-radius:4px}
.hot-head{height:45px;background:linear-gradient(#1c8fd4,#0b6ab0);border-radius:4px 4px 0 0;color:#fff;font-family:"PT Sans",Arial,sans-serif;font-weight:700;font-size:25px;padding:6px 0 0 19px}
.news{position:absolute;left:18px;width:386px;height:94px;border-bottom:1px dotted #aaa}
.date{position:absolute;left:0;top:12px;width:64px;height:66px;background:#fff;box-shadow:0 1px 3px rgba(0,0,0,.25);text-align:center;font-family:"Gelasio",Georgia,serif}
.date .m{display:block;color:var(--blue-text);font-size:17px;padding-top:8px;line-height:18px}
.date .d{display:block;color:var(--orange);font-size:27px;line-height:28px}
.news h3{position:absolute;left:80px;top:10px;font-family:"Gelasio",Georgia,serif;font-weight:400;font-size:18px;color:var(--blue-text);white-space:nowrap}
.news p{position:absolute;left:80px;top:37px;width:290px;font-size:12.5px;line-height:16px;color:#555;white-space:nowrap}
.news .go{position:absolute;right:0;top:36px}
.all-news{position:absolute;left:0;width:100%;top:342px;text-align:center;font-family:"Gelasio",Georgia,serif;font-size:19px;color:var(--orange);display:flex;justify-content:center;align-items:center;gap:7px;white-space:nowrap}

/* footer */
.footer-title{position:absolute;left:142px;top:1013px;font-family:"Gelasio",Georgia,serif;font-size:18px;color:var(--gold)}
.footer-col{position:absolute;top:1041px;font-size:11.5px;line-height:17px;color:var(--text-light);white-space:nowrap}
.footer-col .label{color:var(--gold)}
.partner{position:absolute;top:1038px;height:68px;background:#fff}
.footer-rule{position:absolute;left:142px;top:1128px;width:918px;height:1px;background:rgba(255,255,255,.12)}
.copyright{position:absolute;left:142px;top:1145px;font-size:11.5px;color:var(--text-light)}
.follow{position:absolute;left:883px;top:1139px;display:flex;align-items:center;gap:10px;font-family:"Gelasio",Georgia,serif;font-size:13px;color:#fff}
.follow i{display:block;width:30px;height:30px;border-radius:50%;background:#f4f4f4;border:2px solid #d8d0c8}
</style>
</head>
<body>
<div class="band-top"></div>
<div class="band-footer"></div>

<header>
  <div class="header"></div>
  <div class="logo-tab"></div>
  <div class="logo">BROVIN</div>
  <div class="top-links">
    <div class="top-link" style="width:176px"><svg width="20" height="14" viewBox="0 0 20 14"><rect width="20" height="14" rx="1" fill="#d9432a"/><path d="M1 1l9 7 9-7" stroke="#fff" stroke-width="1.6" fill="none"/></svg>Subscribe Newsletter</div>
    <div class="top-link" style="width:108px;margin-left:9px"><svg width="16" height="13" viewBox="0 0 18 14"><path d="M1 5c0-3 16-3 16 0v2h-4V5H5v2H1z" fill="#666"/><rect x="3" y="7" width="12" height="7" rx="1" fill="#666"/></svg>Contact Us</div>
    <div class="top-link" style="width:96px;margin-left:13px"><svg width="16" height="16" viewBox="0 0 16 16"><rect x="1" y="1" width="14" height="14" rx="2" fill="none" stroke="#666" stroke-width="1.5"/><rect x="4" y="4" width="3" height="3" fill="#666"/><rect x="9" y="4" width="3" height="3" fill="#666"/><rect x="4" y="9" width="3" height="3" fill="#666"/><rect x="9" y="9" width="3" height="3" fill="#666"/></svg>Site Map</div>
  </div>
  <nav class="nav">
    <div class="nav-home"><svg width="30" height="26" viewBox="0 0 30 26"><path d="M15 2L2 13h4v11h7v-7h4v7h7V13h4z" fill="#fff"/></svg></div>
    <div class="nav-item" style="width:152px"><b>The Philosophy</b><span>Company Info</span></div>
    <div class="nav-item active" style="width:230px"><b>Our Solutions</b><span>In cludes PDFs &amp; Vidora Videos</span></div>
    <div class="nav-item" style="width:243px"><b>Our Protfolios</b><span>Photo Gallery with Descriptions</span></div>
    <div class="nav-item last" style="width:233px"><b>Contact Us</b><span>With Categorized Submissions</span></div>
  </nav>
</header>

<main>
  <section class="slider"></section>
  <div class="slide-photo" role="img" aria-label="Photo of a bright modern living room with black sofas and armchairs beside tall windows"></div>
  <div class="slide-title">Featured solution</div>
  <div class="slide-dots"><i></i><i></i><i></i></div>
  <div class="slide-caption">Lorem Ipsum is simply dummy text of the printing and type setting industry. Lorem Ipsum has been the industry's standard dummy text ever since the 1500s,<br>when an unknown printer took a galley of type and scrambled it to make a type specimen book.</div>

  <ul class="dropdown">
    <li class="current">Glass &amp; Glazing</li>
    <li>Building Services</li>
    <li>Filtration</li>
    <li>Automotives</li>
    <li>Others</li>
  </ul>
  <ul class="submenu">
    <li>Sun Control Films</li>
    <li>Safety Films</li>
  </ul>

  <section class="content"></section>
  <div class="portfolio-photo" role="img" aria-label="Photo of suburban houses with green lawns along a curving street under a blue sky"></div>
  <div class="portfolio-badge">FEATURED<br>PORTFOLIO</div>
  <div class="view-more">View More <svg width="5" height="8" viewBox="0 0 5 8"><path d="M0 0l5 4-5 4z" fill="#555"/></svg></div>

  <section class="hot">
    <div class="hot-head">What’s Hot!</div>
    <article class="news" style="top:48px">
      <div class="date"><span class="m">JUL</span><span class="d">15</span></div>
      <h3>Contrary to popular</h3>
      <p>Lorem Ipsum is simply dummy text of the print-<br>ing and typesetting industry.</p>
      <svg class="go" width="14" height="14" viewBox="0 0 14 14"><circle cx="7" cy="7" r="7" fill="#cfcfcf"/><path d="M5.5 4l3 3-3 3" stroke="#fff" stroke-width="1.6" fill="none"/></svg>
    </article>
    <article class="news" style="top:142px">
      <div class="date"><span class="m">JUL</span><span class="d">15</span></div>
      <h3>Contrary to popular</h3>
      <p>Lorem Ipsum is simply dummy text of the print-<br>ing and typesetting industry.</p>
      <svg class="go" width="14" height="14" viewBox="0 0 14 14"><circle cx="7" cy="7" r="7" fill="#cfcfcf"/><path d="M5.5 4l3 3-3 3" stroke="#fff" stroke-width="1.6" fill="none"/></svg>
    </article>
    <article class="news" style="top:236px">
      <div class="date"><span class="m">JUL</span><span class="d">15</span></div>
      <h3>Contrary to popular</h3>
      <p>Lorem Ipsum is simply dummy text of the print-<br>ing and typesetting industry.</p>
      <svg class="go" width="14" height="14" viewBox="0 0 14 14"><circle cx="7" cy="7" r="7" fill="#cfcfcf"/><path d="M5.5 4l3 3-3 3" stroke="#fff" stroke-width="1.6" fill="none"/></svg>
    </article>
    <div class="all-news">See All Upcoming News <svg width="16" height="16" viewBox="0 0 16 16"><circle cx="8" cy="8" r="8" fill="#e8501a"/><path d="M6.5 4.5l3.5 3.5-3.5 3.5" stroke="#fff" stroke-width="2" fill="none"/></svg></div>
  </section>
</main>

<footer>
  <div class="footer-title">Contact Us</div>
  <div class="footer-col" style="left:142px">Brovin Pte Ltd<br>No. 14 Tavern Lane<br>#03-11 Orin Logistics Hub<br>Singapore 548213</div>
  <div class="footer-col" style="left:329px">Telephone: (65) 6400 1123<br>Facsimile: (65) 6400 1124<br>Email: sales@brovin.com.sg</div>
  <div class="footer-col" style="left:499px"><span class="label">OPERATING HOURS:</span><br>Mon-Fri – 8:30am to 5:30pm<br>Sat – 8:30am to 12:30pm<br>Sun &amp; Public Holidays – Closed</div>
  <div class="partner" style="left:692px;width:202px" role="img" aria-label="Authorized distributor badge"></div>
  <div class="partner" style="left:904px;width:154px" role="img" aria-label="Industry association member badge"></div>
  <div class="footer-rule"></div>
  <div class="copyright">Copyright© 2012 Brovin. All Right Reserved.</div>
  <div class="follow">Follow Us <i aria-label="Social link"></i><i aria-label="Social link"></i><i aria-label="Social link"></i></div>
</footer>
</body>
</html>
```